Software Platform User Guide (Manual)

We need a user manual template for our online e-learning platform, Lectern, which allows users to create their own online courses.

We’re looking for a template for a few pages, including a cover, back page, table of contents, and pages for text-only (or bullet points), and text & images (screenshots). We would like to be able to add new pages and adjust textual content ourselves. Lorem ipsum is totally cool as placeholder text. The name of the product is Lectern, but the company name is Mutual Cadence, so we would like the cover and back cover to say “Mutual Cadence" and "Lectern".

We have uploaded a few files to give you a sense of our color scheme and logo. You can also check out our website at mcvista.example for an idea of our aesthetic sensibility. The design should be simple and elegant, and (being a user manual) clarity is king. We use Avenir and Elizabeth as or primary fonts. We have also uploaded some sample screen shots from Lectern. You can use those screenshots to help direct your work, but note that the interface design is changing soon; i.e., you should emphasize the Mutual Cadence brand aesthetic more so than the Lectern user interface design.

Target Market(s)

Businesses and nonprofits looking to implement our platform. Many buyers are female, but the people reading the manual are typically male.

Industry/Entity Type

It Company

Requirements
Must have
• The final product must be a template that will work in Microsoft Word, PowerPoint, or Apple Keynote/Pages. It's fine to send PDFs for previews. Note we need the final product in ONE of the above choices (Word, Powerpoint, Keynote, or Pages), not ALL.

You must make use of the MC logo and fonts on every page. Note that the tag line, "shortest distance between two points of view" in one version of the logo does note have to be included.

We need clear delineation between headers, sub-headers, and bullets, as well as a great looking cover, table of contents and back page.

Please Note: Please disregard the OLVA logo on any screenshots. These were mockups for a client. Please don't use the OLVA name or logo.

```html
<!DOCTYPE html>
<html lang="en">
<head>
<meta charset="utf-8">
<title>Lectern User Manual – Template Spreads</title>
<link rel="stylesheet" href="https://fonts.googleapis.com/css2?family=Crimson+Text:wght@400;600;700&family=Nunito+Sans:wght@400;700;800&display=swap">
<style>
  :root{
    --navy:#233d5c;
    --navy-deep:#1d3450;
    --blue:#4d8bcc;
    --green:#b3cd2b;
    --paper:#f1f1f1;
    --white:#ffffff;
    --ink:#3a4a5e;
    --orange:#f26b2a;
    --ui-dark:#2f2f2f;
    --ui-grey:#8a8a8a;
    --backdrop:#d8d3cb;
    --serif:"Crimson Text", Georgia, serif;
    --sans:"Nunito Sans", Arial, sans-serif;
  }
  html,body{margin:0;padding:0;overflow:hidden;}
  body{background:var(--backdrop);}
  .canvas{position:relative;width:842px;height:1200px;overflow:hidden;background:var(--backdrop);font-family:var(--serif);}
  .abs{position:absolute;}
  .spread{position:absolute;background:var(--navy);}
  .spread--cover{left:46px;top:38px;width:730px;height:518px;}
  .spread--inner{left:48px;top:609px;width:729px;height:517px;}
  .fold{position:absolute;top:0;bottom:0;width:1px;background:rgba(255,255,255,.18);}
  .shape{position:absolute;left:0;top:0;overflow:visible;}

  /* back cover */
  .back-band{left:5px;top:164px;width:355px;height:231px;background:var(--blue);}
  .badge{position:absolute;border-radius:50%;background:var(--green);border:3px solid var(--navy-deep);display:flex;align-items:center;justify-content:center;color:var(--navy);font-family:var(--serif);font-weight:700;}
  .back-badge{left:146px;top:120px;width:78px;height:78px;font-size:30px;}
  .back-copy{left:39px;top:246px;width:286px;color:var(--white);font-size:7px;line-height:16px;text-align:justify;margin:0;}
  .address{left:77px;top:420px;color:var(--white);font-size:7.2px;line-height:9.6px;margin:0;}
  .web{color:var(--white);font-size:10.5px;letter-spacing:2.6px;}
  .back-web{left:77px;top:464px;}

  /* front cover */
  .wordmark{left:402px;top:70px;color:var(--green);font-size:26px;font-weight:600;line-height:1;letter-spacing:.5px;}
  .wordmark-sub{left:402px;top:104px;color:var(--blue);font-size:10.5px;letter-spacing:1.6px;}
  .hero-image{left:374px;top:164px;width:346px;height:220px;background:linear-gradient(135deg,#ffffff 0%,#f1f2f4 45%,#d6dbe2 100%);}
  .hero-key{position:absolute;left:165px;top:52px;width:130px;height:78px;border-radius:10px;background:linear-gradient(160deg,#4d9ad9,#2f74b8);transform:rotate(28deg);}
  .manual-title{right:32px;top:419px;color:var(--green);font-size:12.5px;font-weight:700;letter-spacing:2.4px;}
  .front-web{right:32px;top:479px;}

  /* contents page */
  .content-panel{left:5px;top:69px;width:346px;height:231px;background:var(--paper);border-left:4px solid var(--blue);box-sizing:border-box;}
  .inner-badge{left:47px;top:32px;width:64px;height:64px;font-size:24px;}
  .toc-title{left:58px;top:119px;color:var(--blue);font-size:14.5px;letter-spacing:.4px;margin:0;font-weight:400;}
  .toc{left:58px;top:155px;list-style:none;margin:0;padding:0;}
  .toc li{display:flex;align-items:center;height:22px;color:var(--ink);font-size:10.5px;}
  .toc .num{width:15px;height:15px;border-radius:50%;background:var(--green);color:var(--navy);font-size:8.5px;display:flex;align-items:center;justify-content:center;margin-right:45px;}
  .section-title{left:75px;top:320px;color:var(--green);font-size:13.5px;letter-spacing:.3px;margin:0;font-weight:400;}
  .bullets{left:63px;top:345px;list-style:none;margin:0;padding:0;}
  .bullets li{position:relative;padding-left:16px;color:var(--white);font-size:9.3px;line-height:16px;}
  .bullets li::before{content:"";position:absolute;left:1px;top:5.5px;width:5px;height:5px;border-radius:50%;background:var(--blue);}

  /* screens */
  .screen{position:absolute;background:var(--white);font-family:var(--sans);overflow:hidden;}
  .screen--dash{left:415px;top:23px;width:264px;height:227px;}
  .screen--quiz{left:415px;top:260px;width:264px;height:223px;border-right:3px solid var(--green);}
  .ui-bar{height:28px;background:var(--ui-dark);position:relative;}
  .ui-user{position:absolute;right:22px;top:7px;color:#fff;font-size:4.5px;font-weight:800;}
  .ui-avatar{position:absolute;right:60px;top:5px;width:11px;height:11px;background:#777;}
  .ui-nav{position:absolute;left:14px;bottom:3px;color:#ddd;font-size:3.4px;font-weight:700;letter-spacing:.3px;word-spacing:10px;}
  .ui-photo{height:78px;background:linear-gradient(180deg,#5a4a3c,#2e2a28 60%,#3a3330);position:relative;}
  .ui-tag{position:absolute;right:0;top:12px;width:84px;height:20px;background:var(--orange);color:#fff;font-size:6px;padding:3px 5px;box-sizing:border-box;line-height:6.5px;}
  .ui-tag b{font-size:4.5px;}
  .ui-body{display:flex;padding:8px 10px;gap:8px;}
  .ui-col{flex:1;}
  .ui-welcome{color:var(--ui-grey);font-size:6px;margin:0 0 4px;}
  .ui-welcome span{color:var(--orange);}
  .ui-text{color:#aaa;font-size:3.4px;line-height:4.6px;margin:0 0 4px;}
  .ui-btn{display:inline-block;background:var(--orange);color:#fff;font-size:3.8px;font-weight:700;padding:2px 8px;border-radius:2px;}
  .ui-head{color:var(--orange);font-size:4.2px;font-weight:800;margin:0 0 3px;}
  .course{display:flex;gap:4px;margin-bottom:5px;}
  .course-thumb{width:36px;height:20px;background:linear-gradient(135deg,#c9a57c,#7b5a3f);flex:none;}
  .course-title{font-size:3.8px;font-weight:700;color:#333;}
  .course-meta{font-size:3px;color:var(--ui-grey);line-height:4px;}
  .course-meta i{color:var(--orange);font-style:normal;}

  .quiz-title{position:absolute;left:12px;top:7px;font-size:8.5px;font-weight:800;color:#222;}
  .quiz-close{position:absolute;right:14px;top:4px;font-size:10px;color:#333;}
  .quiz-rule{position:absolute;left:12px;right:14px;top:20px;height:1px;background:#ddd;}
  .quiz-label{position:absolute;font-size:5.5px;font-weight:800;color:var(--orange);}
  .quiz-hint{position:absolute;left:26px;top:78px;width:116px;text-align:center;color:#aaa;font-size:7.5px;line-height:7px;}
  .palette{position:absolute;left:160px;top:48px;width:84px;display:grid;grid-template-columns:1fr 1fr;gap:2px;}
  .palette span{border:1px solid #ccc;font-size:3.3px;color:#444;padding:1px 3px;line-height:4px;}
  .palette-note{position:absolute;left:160px;top:108px;width:92px;font-size:3.4px;color:#444;line-height:4.6px;}
  .settings{position:absolute;left:12px;top:142px;width:238px;height:33px;border:1px solid #e4e4e4;}
  .settings-label{position:absolute;left:6px;top:-6px;background:#fff;padding:0 3px;font-size:5px;font-weight:800;color:var(--orange);}
  .settings-field{position:absolute;left:6px;top:10px;font-size:3.6px;font-weight:700;color:#333;}
  .settings-help{position:absolute;left:6px;top:17px;font-size:3px;color:#777;}
  .settings-input{position:absolute;left:84px;top:9px;width:20px;height:6px;border:1px solid #ccc;}
  .save-btn{position:absolute;right:14px;top:186px;width:64px;height:14px;background:var(--orange);border-radius:2px;color:#fff;font-size:5.5px;font-weight:800;display:flex;align-items:center;justify-content:center;}
  .save-alt{position:absolute;right:14px;top:204px;font-size:3.4px;color:#999;text-decoration:underline;}
</style>
</head>
<body>
<div class="canvas">

  <!-- Cover spread: back cover (left) and front cover (right) -->
  <section class="spread spread--cover" aria-label="Cover spread">
    <div class="fold" style="left:364px"></div>

    <!-- back cover -->
    <div class="abs back-band"></div>
    <div class="badge back-badge">MC</div>
    <p class="abs back-copy">Lorem ipsum dolor sit amet, consectetuer adipiscing elit, sed diam nonummy nibh euismod tincidunt ut laoreet dolore magna aliquam erat volutpat. Ut wisi enim ad minim veniam, quis nostrud exerci tation ullamcorper suscipit lobortis nisl ut aliquip ex ea commodo consequat. Duis autem vel eum iriure dolor in hendrerit in vulputate velit esse molestie consequat, vel illum dolore eu feugiat nulla facilisis at vero eros et accumsan et iusto odio dignissim qui blandit praesent luptatum zzril delenit augue duis dolore te feugait nulla facilisi.</p>
    <p class="abs address">Mutual Cadence, LLC.<br>88 Harbor Lane<br>Portland, Oregon 97201<br>+1 555-014-2290</p>
    <div class="abs web back-web">www. mcvista.example</div>

    <!-- front cover -->
    <div class="abs wordmark">Mutual Cadence</div>
    <div class="abs wordmark-sub">user manual for lectern</div>
    <svg class="shape" width="730" height="518" viewBox="0 0 730 518" aria-hidden="true">
      <path d="M369 201 L369 170 C470 168 600 160 700 127 L700 201 Z" fill="var(--blue)"/>
      <rect x="369" y="164" width="5" height="236" fill="var(--blue)"/>
      <rect x="720" y="164" width="5" height="230" fill="var(--green)"/>
      <path d="M394 394 L725 394 L725 400 C620 400 480 408 396 432 Z" fill="var(--green)"/>
    </svg>
    <div class="abs hero-image" role="img" aria-label="Close-up photo of a white keyboard with a blue key labelled Lectern">
      <div class="hero-key"></div>
    </div>
    <div class="abs manual-title">USER MANUAL</div>
    <div class="abs web front-web">www. mcvista.example</div>
  </section>

  <!-- Inner spread: contents page (left) and screenshot page (right) -->
  <section class="spread spread--inner" aria-label="Inner spread">
    <div class="fold" style="left:362px"></div>

    <svg class="shape" width="729" height="517" viewBox="0 0 729 517" aria-hidden="true">
      <path d="M60 72 C170 66 320 58 378 32 L378 69 L60 69 Z" fill="var(--blue)"/>
      <path d="M430 483 L682 483 L682 488 C600 490 500 496 432 512 Z" fill="var(--green)"/>
    </svg>
    <div class="abs content-panel"></div>
    <div class="badge inner-badge">MC</div>
    <h2 class="abs toc-title">CONTENT</h2>
    <ol class="abs toc">
      <li><span class="num">1</span>Lorem ipsum dolor</li>
      <li><span class="num">2</span>Lorem ipsum dolor</li>
      <li><span class="num">3</span>Lorem ipsum dolor</li>
      <li><span class="num">4</span>Lorem ipsum dolor</li>
      <li><span class="num">5</span>Lorem ipsum dolor</li>
    </ol>
    <h3 class="abs section-title">LOREM IPSUM DOLOR</h3>
    <ul class="abs bullets">
      <li>Lorem ipsum dolor sit amet, consectetuer adipiscing elit, sed</li>
      <li>Diam nonummy nibh euismod tincidunt ut laoreet dolore</li>
      <li>Magna aliquam erat volutpat. Ut wisi enim ad minim veniam,</li>
      <li>Quis nostrud exerci tation ullamcorper suscipit lobortis nisl ut</li>
      <li>Aliquip ex ea commodo consequat. Duis autem vel eum</li>
      <li>Giure dolor in hendrerit in vulputate velit esse molestie</li>
      <li>Dequat, velim qui blandit praesent luptatum zzril delenit</li>
      <li>Bugue duis dolore te feugait nulla facilisi.</li>
    </ul>

    <!-- dashboard screenshot -->
    <div class="screen screen--dash">
      <div class="ui-bar">
        <div class="ui-avatar"></div>
        <div class="ui-user">JORDAN VALE</div>
        <div class="ui-nav">HOME DASHBOARD COURSES CONTACT</div>
      </div>
      <div class="ui-photo" role="img" aria-label="Photo of a student reading in a library">
        <div class="ui-tag">NOW ENROLLING<br><b>SUMMER 2013 COURSES</b></div>
      </div>
      <div class="ui-body">
        <div class="ui-col">
          <p class="ui-welcome">Welcome, <span>User!</span></p>
          <p class="ui-text">Lorem ipsum dolor sit amet, consectetur adipiscing elit, sed do eiusmod tempor incididunt ut labore et dolore magna aliqua. Ut enim ad minim veniam, quis nostrud exercitation ullamco laboris nisi ut aliquip ex ea commodo consequat.</p>
          <p class="ui-text">Duis aute irure dolor in reprehenderit in voluptate velit esse cillum dolore eu fugiat nulla pariatur. Excepteur sint occaecat cupidatat non proident, sunt in culpa qui officia deserunt mollit anim id est laborum.</p>
          <span class="ui-btn">Create a Course</span>
        </div>
        <div class="ui-col">
          <p class="ui-head">MY COURSES</p>
          <div class="course"><div class="course-thumb" role="img" aria-label="Course thumbnail photo"></div><div><div class="course-title">This is a course title</div><div class="course-meta">Status: 2 students await review<br>Professor: Sam Reed<br><i>Go to course</i></div></div></div>
          <div class="course"><div class="course-thumb" role="img" aria-label="Course thumbnail photo"></div><div><div class="course-title">This is a course title and it's long</div><div class="course-meta">Progress: In Progress<br>Professor: Sam Reed<br><i>Go to course</i></div></div></div>
        </div>
      </div>
    </div>

    <!-- quiz builder screenshot -->
    <div class="screen screen--quiz">
      <div class="quiz-title">Create Quiz</div>
      <div class="quiz-close">×</div>
      <div class="quiz-rule"></div>
      <div class="quiz-label" style="left:12px;top:35px">Quiz Preview</div>
      <div class="quiz-label" style="left:160px;top:35px">Add Questions</div>
      <div class="quiz-hint">Drag fields from the palette to create your quiz</div>
      <div class="palette">
        <span>Textfield</span><span>Number</span>
        <span>Multiple choice, single answer</span><span>Multiple choice, multiple answers</span>
        <span>Select list</span><span>Date</span>
        <span>Time</span><span>Description</span>
        <span>Page break</span>
      </div>
      <div class="palette-note">Drag the quiz questions to the preview area on the left. "Page break" will break the quiz up into two pages.</div>
      <div class="settings">
        <span class="settings-label">Quiz Settings</span>
        <span class="settings-field">Percent Correct</span>
        <span class="settings-input"></span>
        <span class="settings-help">Enter the percentage a user must answer correctly to pass.</span>
      </div>
      <div class="save-btn">Save Quiz</div>
      <div class="save-alt">Or save and Add your first Lesson</div>
    </div>
  </section>

</div>
</body>
</html>
```